Website redesign for a national printing company

Our current website is dated and boring: ridgefieldpennants.com

We are looking for a fresh, modern design. We need a clean, minimal design that is also elegant, really shows off large, bright photos of our banners in action and POPS. Our goal is to showcase our beautiful banners, while also giving the user the confidence in our company that we will provide friendly, fast service, fast printing, and deliver their banners on time for their event.

I want a nice flow to the website, the design should tie in well with the printing feel. Here is an example of clean, beautiful design that ties in to the industry - https://www.vorly.com/ - notice how the buttons are like chat icons, for example.

More examples:

Nice clean design https://www.plimbask.com/

https://grevaltic.com/ nice and clean, but it POPS really well.

I like https://www.tarmenvok.com/

https://www.wobrel.com/ gorgeous site, clean, modern

Beautiful, simple, clean, modern - https://fenquatro.com/en-us/

These websites are not from the print industry, that’s because most printers don’t have good websites - they are more focused on local businesses, referrals, not really online marketing.

But keep in mind in your design that we need to give the feel that we are printing their banners beautifully, fast, with great service.

https://www.ambergrale.com/ so clean, bold, clear to the user what the company does. Love this simple yet elegant design.

https://www.q7.com/ - so pretty! And still so simple and obvious to the user what to do on their site.

https://zolvex.com/

https://quarnelby.com/us/en/ big and bold - yet super nicely designed with so many nice touches

https://postwrenly.com/ - also clean, simple, and so obvious to the user to take action and contact the company
Updates

I just updated the job brief, and you can also view it in full here - https://files.vendrolax.com/document/d/7Rmq3ZTp9Lx2Nb8Ck4Hs6Wv0Jd5Fy1Ga3Ue8Oi2Pt/edit?usp=sharing

Target Market(s)

Please read this customer persona - https://files.vendrolax.com/document/d/7Rmq3ZTp9Lx2Nb8Ck4Hs6Wv0Jd5Fy1Ga3Ue8Oi2Pt/edit?usp=sharing

Industry/Entity Type

Printing

Number of Pages Required

1 page

Requirements
Must have
• Nice flow to the website, the design should tie in well with the printing feel. Here is an example of clean, beautiful design that ties in to the industry - https://www.vorly.com/ - notice how the buttons are like chat icons, for example.
Should not have
• No filters on the images, we want large, beautiful images.

```html
<!DOCTYPE html>
<html lang="en">
<head>
<meta charset="utf-8">
<title>Ridgefield Pennants</title>
<link href="https://fonts.googleapis.com/css2?family=Josefin+Sans:wght@400;600;700&family=Libre+Baskerville:wght@400;700&display=swap" rel="stylesheet">
<style>
:root{
  --purple:#5a3fda;
  --green:#07d98f;
  --ink:#1d1d1f;
  --muted:#555;
  --hero-bg:#f6f6f7;
  --lavender:#eeeefb;
  --peach:#fbe8da;
  --footer:#1c1c1d;
}
*{box-sizing:border-box;margin:0;padding:0}
html,body{width:1200px;height:3257px;overflow:hidden}
body{position:relative;font-family:"Josefin Sans",sans-serif;color:var(--ink);background:#fff}
.abs{position:absolute}
.serif{font-family:"Libre Baskerville",serif;font-weight:400}
.btn{position:absolute;display:flex;align-items:center;justify-content:center;border-radius:20px;font-size:11px;font-weight:600;color:#fff;background:var(--purple)}
.btn.dark{background:var(--ink)}

/* header */
.site-header{position:absolute;left:0;top:0;width:1200px;height:75px;background:#fff;box-shadow:0 2px 8px rgba(0,0,0,.04)}
.brand{position:absolute;left:94px;top:18px;color:var(--purple)}
.brand-name{font-size:25px;font-weight:700;letter-spacing:-.3px;line-height:1}
.brand-sub{font-size:9px;letter-spacing:5px;margin-top:4px;padding-left:22px}
.nav a{position:absolute;top:31px;font-size:11px;color:var(--ink);text-decoration:none}
.nav a.active{color:var(--green)}
.toll{position:absolute;left:705px;top:31px;font-size:11px;color:var(--green)}
.toll b{color:var(--ink);font-weight:400;margin-left:6px}
.login{position:absolute;left:860px;top:31px;font-size:11px}

/* hero */
.hero{position:absolute;left:0;top:75px;width:1200px;height:422px;background:var(--hero-bg);overflow:hidden}
.hero h1{position:absolute;left:94px;top:111px;font-size:33px;line-height:45px;width:400px;letter-spacing:-.3px}

/* about */
.about h2{position:absolute;left:0;width:1200px;top:553px;text-align:center;font-size:27px}
.about p{position:absolute;left:250px;width:700px;top:598px;text-align:center;font-size:12.5px;line-height:19px;color:#333}

/* why */
.why{position:absolute;left:0;top:752px;width:1200px;height:537px;background:var(--lavender)}
.why-photo{position:absolute;left:0;top:63px;width:550px;height:411px;border-radius:0 0 28px 0;background:linear-gradient(160deg,#cfd9e6 0%,#7d93b6 35%,#2e3f86 60%,#1a1f3d 100%)}
.why h2{position:absolute;left:613px;top:76px;font-size:27px}
.feature{position:absolute;left:612px;width:360px}
.feature .ico{position:absolute;left:0;top:0;width:50px;height:50px;border-radius:50%;background:var(--ink);display:flex;align-items:center;justify-content:center}
.feature .ico.on{background:var(--purple)}
.feature h3{position:absolute;left:63px;top:4px;font-size:13px;font-weight:400}
.feature p{position:absolute;left:63px;top:22px;font-size:9.5px;line-height:15px;color:#444;width:270px}

/* products */
.products h2{position:absolute;left:0;width:1200px;top:1345px;text-align:center;font-size:27px}
.card{position:absolute;top:1403px;width:234px;height:307px;border-bottom:2px solid var(--ink)}
.card .pic{width:234px;height:155px;border-radius:10px 10px 0 0}
.card h3{margin:20px 18px 0;font-size:13.5px;font-weight:400;line-height:17px;height:34px}
.card h3.one{height:17px}
.card p{margin:14px 18px 0;font-size:9.5px;line-height:15px;color:#444;height:50px}
.card p.long{height:60px}
.card a{display:block;margin:10px 18px 0;font-size:10px;color:var(--purple);text-decoration:none}

/* reviews */
.reviews{position:absolute;left:0;top:1771px;width:1200px;height:499px;background:var(--peach)}
.reviews h2{position:absolute;left:0;width:1200px;top:60px;text-align:center;font-size:27px}
.reviews .sub{position:absolute;left:330px;width:540px;top:106px;text-align:center;font-size:12px;line-height:15px;color:#333}
.review{position:absolute;top:160px;width:249px;height:148px;background:#fff}
.review .stars{position:absolute;left:19px;top:22px;color:#f5a623;font-size:11px;letter-spacing:1px}
.review p{position:absolute;left:19px;top:45px;width:215px;font-size:10.3px;line-height:19px;color:#333}
.review .notch{position:absolute;left:40px;bottom:-10px;width:0;height:0;border-left:10px solid transparent;border-right:10px solid transparent;border-top:10px solid #fff}
.who{position:absolute;top:328px}
.who .av{position:absolute;left:0;top:0;width:38px;height:38px;border-radius:50%;background:linear-gradient(135deg,#c9b6a6,#6e5a4f)}
.who .nm{position:absolute;left:50px;top:8px;font-size:11.5px;white-space:nowrap}
.who .tm{position:absolute;left:50px;top:24px;font-size:9.5px;color:#555;white-space:nowrap}

/* seen in */
.seen h2{position:absolute;left:0;width:1200px;top:2327px;text-align:center;font-size:27px}
.mark{position:absolute;top:2386px;width:148px;height:92px;background:#fff;box-shadow:0 1px 6px rgba(0,0,0,.09);display:flex;align-items:center;justify-content:center;font-size:15px;font-weight:600;color:#6b6b6b}

/* band */
.band{position:absolute;left:0;top:2579px;width:1200px;height:376px;background:var(--green)}
.band h2{position:absolute;left:94px;top:60px;font-size:33px;line-height:45px;color:#1c2b26}
.band h2 b{font-weight:700}
.band p{position:absolute;left:94px;top:213px;font-size:18px;line-height:23px;color:#1c2b26;width:360px;font-weight:400}
.band-photo{position:absolute;left:612px;top:32px;width:588px;height:313px;border-radius:22px 0 0 22px;background:radial-gradient(ellipse at 45% 35%,#c8331c 0%,#8d1b10 45%,#2a0b08 100%)}

/* footer */
.site-footer{position:absolute;left:0;top:2955px;width:1200px;height:302px;background:var(--footer);color:#fff}
.site-footer .brand{left:201px;top:72px;color:#fff}
.site-footer h4{position:absolute;top:62px;font-size:13px;font-weight:600;font-family:"Libre Baskerville",serif}
.contact-line{position:absolute;left:406px;font-size:14px;display:flex;align-items:center;gap:10px}
.contact-line small{font-size:11px}
.links a{position:absolute;font-size:9.5px;color:#ddd;text-decoration:none}
.social{position:absolute;left:968px;width:30px;height:30px;border-radius:50%;background:#fff}
.social.on{background:var(--green)}
.rule{position:absolute;left:201px;top:240px;width:799px;height:1px;background:#444}
.copy{position:absolute;left:0;width:1200px;top:266px;text-align:center;font-size:9.5px;color:#ddd}
.copy span{color:var(--green)}
</style>
</head>
<body>

<header class="site-header">
  <div class="brand"><div class="brand-name">Ridgefield</div><div class="brand-sub">PENNANTS</div></div>
  <nav class="nav">
    <a class="active" style="left:329px">Home</a>
    <a style="left:380px">About</a>
    <a style="left:432px">Products ▾</a>
    <a style="left:511px">Galleries ▾</a>
    <a style="left:588px">Contact Us</a>
  </nav>
  <div class="toll">Toll Free ✆ <b>800-555-0142</b></div>
  <div class="login">👤︎ Login</div>
  <div class="btn dark" style="left:919px;top:22px;width:80px;height:31px">⬆ Upload</div>
  <div class="btn" style="left:1012px;top:22px;width:94px;height:31px">Get a Quote</div>
</header>

<section class="hero">
  <h1 class="serif">We are printing banners beautifully, fast, with great service.</h1>
  <div class="btn" style="left:94px;top:271px;width:93px;height:31px">Get a Quote</div>
  <svg class="abs" style="left:600px;top:0" width="600" height="422" role="img" aria-label="Large roadside billboard banner against a blue sky">
    <defs><linearGradient id="sky" x1="0" y1="0" x2="1" y2="1"><stop offset="0" stop-color="#2f5f93"/><stop offset=".5" stop-color="#7aa3cb"/><stop offset="1" stop-color="#c9d9ea"/></linearGradient></defs>
    <path d="M120 0 H600 V422 H330 C260 330 160 250 70 220 C10 200 0 120 40 70 C70 30 95 10 120 0 Z" fill="url(#sky)"/>
  </svg>
</section>

<section class="about">
  <h2 class="serif">About Ridgefield Pennants</h2>
  <p>For over two decades, Ridgefield Pennants has been the go-to source for high-quality custom printing for large format banners, plastic roll banners, stage backdrops and mobile stage festival banners.</p>
  <div class="btn dark" style="left:550px;top:659px;width:100px;height:30px">Explore More</div>
</section>

<section class="why">
  <div class="why-photo" role="img" aria-label="Two-storey event structure wrapped in a large navy printed banner"></div>
  <h2 class="serif">Why choose us</h2>
  <div class="feature" style="top:139px"><div class="ico"><svg width="20" height="20" viewBox="0 0 20 20" fill="none" stroke="#fff" stroke-width="1.5"><path d="M3 8l4-3 3 2 3-2 4 3-7 6z"/></svg></div><h3>Friendly</h3><p>Excepteur sint occaecat cupidatat proident, sunt in culpa qui officia deserunt ...</p></div>
  <div class="feature" style="top:207px"><div class="ico on"><svg width="20" height="20" viewBox="0 0 20 20" fill="none" stroke="#fff" stroke-width="1.5"><circle cx="10" cy="6" r="3"/><circle cx="5" cy="14" r="3"/><circle cx="15" cy="14" r="3"/></svg></div><h3>Fast Service</h3><p>Excepteur sint occaecat cupidatat proident, sunt in culpa qui officia deserunt ...</p></div>
  <div class="feature" style="top:276px"><div class="ico"><svg width="20" height="20" viewBox="0 0 20 20" fill="none" stroke="#fff" stroke-width="1.5"><rect x="6" y="3" width="8" height="4"/><rect x="3" y="7" width="14" height="7" rx="1"/><rect x="6" y="12" width="8" height="5"/></svg></div><h3>Fast Printing</h3><p>Excepteur sint occaecat cupidatat proident, sunt in culpa qui officia deserunt ...</p></div>
  <div class="feature" style="top:345px"><div class="ico"><svg width="22" height="20" viewBox="0 0 22 20" fill="none" stroke="#fff" stroke-width="1.5"><rect x="2" y="5" width="11" height="9"/><path d="M13 8h4l3 3v3h-7z"/><circle cx="6" cy="15" r="1.6"/><circle cx="16" cy="15" r="1.6"/></svg></div><h3>Deliver Their Banners on Time</h3><p>Excepteur sint occaecat cupidatat proident, sunt in culpa qui officia deserunt ...</p></div>
  <div class="btn" style="left:613px;top:426px;width:92px;height:30px">Get a Quote</div>
</section>

<section class="products">
  <h2 class="serif">Our products</h2>
  <div class="card" style="left:94px"><div class="pic" role="img" aria-label="Plastic roll banners along a fence at an outdoor event" style="background:linear-gradient(180deg,#c8d4e0,#9a9a9a 55%,#2b2b2b)"></div><h3 class="one">Plastic Roll Banners</h3><p class="long">Plastic Roll Banners offer an economical and effective way to communicate your marketing message at concerts, sporting events, radio station events ...</p><a>Read More →</a></div>
  <div class="card" style="left:353px"><div class="pic" role="img" aria-label="Festival stage with large printed backdrops at dusk" style="background:linear-gradient(180deg,#6f7fc0,#d98aa0 50%,#3c4a3a)"></div><h3>Festival Banners and Stage Backdrops</h3><p>Great for large backdrops and stage scrims at outdoor festivals or concerts. The mesh allows for air to flow through ...</p><a>Read More →</a></div>
  <div class="card" style="left:612px"><div class="pic" role="img" aria-label="Large mesh banner on a building facade" style="background:linear-gradient(180deg,#6a8fb8,#8fbf5a 45%,#214060)"></div><h3>Large Format and Mesh Banners</h3><p>Transform any space with your brand on mesh banners. Digitally printed and fully customizable, mesh banners ...</p><a>Read More →</a></div>
  <div class="card" style="left:871px"><div class="pic" role="img" aria-label="Cloth backdrop in a hall with rows of seating" style="background:linear-gradient(180deg,#3a3a44,#7a6a6a 50%,#2a2a34)"></div><h3>Cloth Banners and Cloth Backdrops</h3><p>Cloth banners are the ultimate gold standard in backdrop printing. With vibrant color representation, high definition ...</p><a>Read More →</a></div>
</section>

<section class="reviews">
  <h2 class="serif">Rated 5/5 stars by our customers</h2>
  <div class="sub">Read our Findora reviews and see why radio stations, festival organizers, bands and many other companies love Ridgefield Pennants.</div>
  <svg class="abs" style="left:137px;top:234px" width="10" height="12"><path d="M7 1L2 6l5 5" stroke="#555" fill="none" stroke-width="1.5"/></svg>
  <svg class="abs" style="left:1053px;top:234px" width="10" height="12"><path d="M3 1l5 5-5 5" stroke="#5a3fda" fill="none" stroke-width="1.5"/></svg>
  <div class="review" style="left:201px"><div class="stars">★★★★★</div><p>“The banner turned out great and was delivered promptly. Looks great at gigs. Jenna Marsh, Rusty Hinge and the Lowlanders”</p><div class="notch"></div></div>
  <div class="review" style="left:475px"><div class="stars">★★★★★</div><p>“Ridgefield was great to work with. We used them to make banners for our outdoor graduation in Atlanta. They assisted with artwork, were super...”</p><div class="notch"></div></div>
  <div class="review" style="left:751px"><div class="stars">★★★★★</div><p>“Corin and the team at Ridgefield Pennants have been great to work with. Their eye to detail is spot on. Don't be afraid to ask as many...”</p><div class="notch"></div></div>
  <div class="who" style="left:226px"><div class="av" role="img" aria-label="Reviewer avatar"></div><div class="nm">Dana Whitlow</div><div class="tm">1 month ago</div></div>
  <div class="who" style="left:501px"><div class="av" role="img" aria-label="Reviewer avatar"></div><div class="nm">Lorna P</div><div class="tm">2 months ago</div></div>
  <div class="who" style="left:775px"><div class="av" role="img" aria-label="Reviewer avatar"></div><div class="nm">Miles Corrigan</div><div class="tm">4 months ago</div></div>
  <div class="btn dark" style="left:550px;top:404px;width:100px;height:31px">View All</div>
</section>

<section class="seen">
  <h2 class="serif">As seen in</h2>
  <div class="mark" style="left:201px">Brightwave</div>
  <div class="mark" style="left:363px">Tallis Radio</div>
  <div class="mark" style="left:525px">Ferro Hoops</div>
  <div class="mark" style="left:688px">Kestrel Media</div>
  <div class="mark" style="left:849px">Ambrel Foods</div>
  <svg class="abs" style="left:576px;top:2507px" width="48" height="12">
    <circle cx="5" cy="6" r="3.5" fill="none" stroke="#5a3fda"/>
    <circle cx="17" cy="6" r="4" fill="none" stroke="#5a3fda"/><circle cx="17" cy="6" r="2" fill="#5a3fda"/>
    <circle cx="29" cy="6" r="3.5" fill="none" stroke="#5a3fda"/>
    <circle cx="41" cy="6" r="3.5" fill="none" stroke="#5a3fda"/>
  </svg>
</section>

<section class="band">
  <h2 class="serif"><b>Are you a Band?</b><br>take your shows to the<br>next level</h2>
  <p>Contact our product experts for all your pricing and sizing needs.</p>
  <div class="btn" style="left:95px;top:280px;width:155px;height:30px">stagedropsforbands.com</div>
  <div class="band-photo" role="img" aria-label="Red cloth stage backdrop behind a drum kit"></div>
</section>

<footer class="site-footer">
  <div class="brand"><div class="brand-name">Ridgefield</div><div class="brand-sub">PENNANTS</div></div>
  <h4 style="left:406px">Contact Us</h4>
  <div class="contact-line" style="top:94px"><span style="color:var(--green)">✆</span>800-555-0142</div>
  <div class="contact-line" style="top:117px"><span style="color:var(--green)">✆</span>734-555-0198 <small>(Local and Canada)</small></div>
  <div class="contact-line" style="top:142px;font-size:11px"><span style="color:var(--green)">✉</span>info@ridgefieldpennants.com</div>
  <h4 style="left:681px">Quick Links</h4>
  <div class="links">
    <a style="left:681px;top:97px">Request a Catalog</a>
    <a style="left:681px;top:116px">Blogs</a>
    <a style="left:681px;top:135px">FAQ</a>
    <a style="left:681px;top:154px">Stagedropsforbands.com</a>
    <a style="left:681px;top:173px">Customer Reviews</a>
    <a style="left:817px;top:97px">Customer Sales Contract</a>
    <a style="left:817px;top:116px">Privacy Policy</a>
    <a style="left:817px;top:135px">Contact Us</a>
  </div>
  <div class="social" style="top:64px"></div>
  <div class="social on" style="top:102px"></div>
  <div class="social" style="top:140px"></div>
  <div class="rule"></div>
  <div class="copy">© 2023 <span>Ridgefield Pennants</span>. All Rights Reserved</div>
</footer>

</body>
</html>
```